K & M Wheel Depot business cards

need business card for tire/car care company based in tampa, florida. we sell used and new tires, also we service vehicles, tune ups, oil chasnge, brakes and A/c we offer free towing with major vehicle repair and tire purchase. we also offer free estimates on any engine or a/c repair. also we have the lowest price in the city on used and new tires.

Contact Information for Business Card

4170 E Marigold Blvd,
Tampa, Fl 33581
Ph: 813-572-3186
KandMWheelDepot@Mailverse.com

Font styles to use
Serif
Sans Serif
Decorative

Requirements
Must have
• my logo, what we do ( used and new tires , oil change, brakes, tune ups, free towing vehicl. Also business info.
Nice to have
• an image of a towing truck, highlighting that we offer free towing. something close to what i have in one of the attached image

```html
<!DOCTYPE html>
<html lang="en">
<head>
<meta charset="utf-8">
<title>K &amp; M Wheel Depot — Business Cards</title>
<link href="https://fonts.googleapis.com/css2?family=Open+Sans:wght@400;600;700&display=swap" rel="stylesheet">
<style>
  :root {
    --bg: #e9e9e7;
    --yellow: #f2c318;
    --black: #0b0b0b;
    --white: #ffffff;
    --photo-light: #dfe3ea;
    --photo-mid: #7d8797;
    --photo-dark: #2d3a63;
  }
  * { box-sizing: border-box; margin: 0; padding: 0; }
  html, body { width: 1200px; height: 800px; overflow: hidden; }
  body {
    background: var(--bg);
    font-family: "Open Sans", Arial, sans-serif;
    display: flex;
    align-items: center;
    justify-content: center;
    gap: 50px;
  }
  .card {
    position: relative;
    width: 525px;
    height: 300px;
    background: var(--yellow);
    overflow: hidden;
    box-shadow: 0 6px 18px rgba(0,0,0,.18);
  }

  /* Front */
  .brand {
    position: absolute;
    top: 62px;
    left: 0; right: 0;
    display: flex;
    align-items: center;
    justify-content: center;
    gap: 14px;
  }
  .brand-dot {
    flex: none;
    width: 34px; height: 34px;
    border-radius: 50%;
    background: var(--black);
  }
  .brand-name {
    font-size: 38px;
    font-weight: 700;
    color: var(--black);
    letter-spacing: -.5px;
    white-space: nowrap;
  }
  .contact-band {
    position: absolute;
    left: 0; right: 0;
    top: 188px;
    height: 86px;
    background: var(--black);
    color: var(--white);
    text-align: center;
    display: flex;
    flex-direction: column;
    justify-content: center;
    gap: 2px;
  }
  .contact-address { font-size: 12px; }
  .contact-phone { font-size: 19px; font-weight: 600; line-height: 1.1; }
  .contact-email { font-size: 12px; }

  /* Back */
  .back-art { position: absolute; inset: 0; }
  .back-brand {
    position: absolute;
    top: 26px;
    right: 22px;
    display: flex;
    align-items: center;
    gap: 8px;
  }
  .back-brand .brand-dot { width: 18px; height: 18px; }
  .back-brand .brand-name { font-size: 17px; letter-spacing: 0; }
  .services {
    position: absolute;
    top: 88px;
    left: 330px;
    right: 18px;
    list-style: none;
    font-size: 12px;
    line-height: 1.4;
    color: var(--black);
  }
  .services li::before { content: "- "; }
</style>
</head>
<body>

  <section class="card card-front">
    <div class="brand">
      <span class="brand-dot"></span>
      <span class="brand-name">K &amp; M Wheel Depot</span>
    </div>
    <div class="contact-band">
      <p class="contact-address">4170 E Marigold Blvd, Tampa, Fl 33581</p>
      <p class="contact-phone">813-572-3186</p>
      <p class="contact-email">KandMWheelDepot@Mailverse.com</p>
    </div>
  </section>

  <section class="card card-back">
    <svg class="back-art" width="525" height="300" viewBox="0 0 525 300">
      <defs>
        <linearGradient id="vehicle-tone" x1="0" y1="0" x2="1" y2="1">
          <stop offset="0" stop-color="#dfe3ea"/>
          <stop offset=".55" stop-color="#7d8797"/>
          <stop offset="1" stop-color="#2d3a63"/>
        </linearGradient>
      </defs>
      <path d="M0 62 Q200 48 292 78 Q335 170 290 300 L0 300 Z" fill="#0b0b0b"/>
      <path d="M0 74 Q195 61 281 89 Q320 172 276 300 L0 300 Z" fill="#ffffff"/>
      <path d="M18 100 Q170 88 262 110 Q295 180 258 288 L18 288 Z"
            fill="url(#vehicle-tone)" role="img"
            aria-label="Photo of a blue tow truck with stacked tires and a wrench"/>
    </svg>
    <div class="back-brand">
      <span class="brand-dot"></span>
      <span class="brand-name">K &amp; M Wheel Depot</span>
    </div>
    <ul class="services">
      <li>Used and new tires</li>
      <li>Oil change</li>
      <li>Brakes</li>
      <li>Tune Ups</li>
      <li>Free Towing with major vehicle Repair</li>
      <li>Tire Purchase</li>
    </ul>
  </section>

</body>
</html>
```